84M business card

I need a business card for a life sciences consulting firm I started. The company name is 84M and the logo is attached. I am looking for something edgey and current but different from the blah standard business card.

Industry/Entity Type

Business

Requirements
Nice to have
• Both sides

```html
<!DOCTYPE html>
<html lang="en">
<head>
<meta charset="utf-8">
<title>84M Business Card</title>
<link rel="stylesheet" href="https://fonts.googleapis.com/css2?family=Open+Sans:wght@400;700&display=swap">
<style>
  :root {
    --stage: #3b3b3d;
    --card: #ffffff;
    --navy: #1f3f8f;
    --orange: #f28a1e;
    --orange-deep: #ee6b1f;
    --ink: #2a2a2a;
    --muted: #8a8a8a;
  }
  * { box-sizing: border-box; margin: 0; padding: 0; }
  html, body {
    width: 1200px; height: 900px; overflow: hidden;
    background: var(--stage);
    font-family: "Open Sans", Arial, sans-serif;
  }
  .canvas { position: relative; width: 1200px; height: 900px; }
  .card {
    position: absolute; width: 620px; height: 354px;
    background: var(--card);
    box-shadow: 0 10px 30px rgba(0,0,0,.35);
    overflow: hidden;
  }
  .card--front { left: 60px; top: 90px; }
  .card--back { left: 520px; top: 456px; }

  .brand { display: flex; align-items: center; gap: 16px; }
  .brand__dot {
    width: 54px; height: 54px; border-radius: 50%;
    background: var(--navy); flex: none;
  }
  .brand__name {
    font-weight: 700; color: var(--navy);
    letter-spacing: 2px; line-height: 1;
  }
  .tagline { color: var(--muted); font-size: 13px; letter-spacing: .3px; }

  .card--front .lockup { position: absolute; left: 150px; top: 70px; }
  .card--front .brand__name { font-size: 72px; }
  .card--front .tagline { margin-top: 6px; margin-left: 70px; }

  .contact {
    position: absolute; left: 290px; top: 205px;
    color: var(--ink); font-weight: 700; font-size: 15px; line-height: 1.3;
    text-transform: uppercase;
  }
  .contact__name { text-align: right; width: 190px; }
  .contact__title { margin-bottom: 18px; }
  .contact__line { font-weight: 400; }

  .card--back .lockup {
    position: absolute; left: 0; right: 0; top: 70px;
    display: flex; flex-direction: column; align-items: center;
  }
  .card--back .brand { flex-direction: column; gap: 14px; }
  .card--back .brand__dot { width: 96px; height: 96px; }
  .card--back .brand__name { font-size: 84px; }
  .card--back .tagline { margin-top: 8px; font-size: 14px; }

  .band { position: absolute; left: 0; bottom: 0; width: 620px; height: 70px; }
</style>
</head>
<body>
<main class="canvas">

  <section class="card card--front">
    <div class="lockup">
      <div class="brand">
        <span class="brand__dot"></span>
        <span class="brand__name">84M</span>
      </div>
      <p class="tagline">regulatory consulting and contract services</p>
    </div>

    <div class="contact">
      <p class="contact__name">Alex Morgan</p>
      <p class="contact__title">Managing Director</p>
      <p class="contact__line">555 210 4471</p>
      <p class="contact__line">alex@84mconsult.com</p>
    </div>

    <svg class="band" viewBox="0 0 620 70" role="img" aria-label="Orange tiled ribbon pattern sweeping along the bottom edge">
      <defs>
        <linearGradient id="bandFront" x1="0" x2="1">
          <stop offset="0" stop-color="#f28a1e"/>
          <stop offset="1" stop-color="#ee6b1f"/>
        </linearGradient>
      </defs>
      <polygon points="0,52 620,14 620,24 0,70" fill="url(#bandFront)"/>
    </svg>
  </section>

  <section class="card card--back">
    <div class="lockup">
      <div class="brand">
        <span class="brand__dot"></span>
        <span class="brand__name">84M</span>
      </div>
      <p class="tagline">regulatory consulting and contract services</p>
    </div>

    <svg class="band" viewBox="0 0 620 70" role="img" aria-label="Orange tiled ribbon pattern sweeping along the bottom edge">
      <defs>
        <linearGradient id="bandBack" x1="0" x2="1">
          <stop offset="0" stop-color="#f28a1e"/>
          <stop offset="1" stop-color="#ee6b1f"/>
        </linearGradient>
      </defs>
      <polygon points="0,52 620,14 620,24 0,70" fill="url(#bandBack)"/>
    </svg>
  </section>

</main>
</body>
</html>
```